Personal Business Card Design Project

I am looking for a business card to be able to hand to both Chinese and Australian businessman.
I am a self employed consultant and just need my name, phone number and email address on the card. No Business Name and No Website.
I want it to look like an exclusive prestigious card.
I would like the background to be be a glossy red and the writing to be gold. (This applies to both sides of the card).
It must have English on one side and Chinese (Mandarin) on the reverse.
Details you will require
Name : Derek Hollins
Phone : + 61 428 903 574
Email : derekhollins@mailvanto.com
Updates
Thank you everybody for your designs.
Industry/Entity Type
Business

```html
<!DOCTYPE html>
<html lang="en">
<head>
<meta charset="utf-8">
<title>Derek Hollins – Business Card</title>
<link rel="stylesheet" href="https://fonts.googleapis.com/css2?family=Tinos:wght@700&display=swap">
<style>
  :root {
    --backdrop: #1c1c1c;
    --card-red-top: #781006;
    --card-red-mid: #960c08;
    --card-red-bottom: #ad0b0b;
    --card-red-edge: #6e0605;
    --gold-light: #fbd25a;
    --gold: #f4b62a;
    --gold-deep: #eda417;
  }

  * { margin: 0; padding: 0; box-sizing: border-box; }

  html, body {
    width: 1200px;
    height: 750px;
    overflow: hidden;
  }

  body {
    background: var(--backdrop);
    display: flex;
    align-items: center;
    justify-content: center;
    font-family: "Tinos", "Times New Roman", serif;
  }

  .business-card {
    position: relative;
    width: 1000px;
    height: 555px;
    background: linear-gradient(
      to bottom,
      var(--card-red-top) 0%,
      var(--card-red-mid) 45%,
      var(--card-red-bottom) 88%,
      var(--card-red-edge) 100%
    );
    box-shadow: 0 10px 30px rgba(0, 0, 0, 0.55);
    display: flex;
    flex-direction: column;
    align-items: center;
    text-align: center;
  }

  .business-card .gold-text {
    font-weight: 700;
    background: linear-gradient(to bottom, var(--gold-light) 0%, var(--gold) 55%, var(--gold-deep) 100%);
    -webkit-background-clip: text;
    background-clip: text;
    color: transparent;
    line-height: 1;
    white-space: nowrap;
  }

  .card-name {
    margin-top: 113px;
    font-size: 92px;
  }

  .card-phone {
    margin-top: 62px;
    font-size: 58px;
  }

  .card-email {
    margin-top: 48px;
    font-size: 48px;
  }
</style>
</head>
<body>
  <section class="business-card" aria-label="Business card">
    <h1 class="card-name gold-text">Derek Hollins</h1>
    <p class="card-phone gold-text">+ 61 428 903 574</p>
    <p class="card-email gold-text">derekhollins@mailvanto.com</p>
  </section>
</body>
</html>
```